Visitenkarten/Briefpaier/Kassenkassenbelege für Juwelier
Zielgruppe
Mittelständischer Juwelier mit zwei Filialen. Klassischer Schmuck, Uhren und Modeschmuck
Aufgabenstellung
Es müssen für zwei Geschäfte Visitenkarten, Briefpapier (A4) und Kassenkassenbelege (A6) erstellt werden. Logo und fenwiro im Anhang. Ein Farbkonzept besteht noch nicht. Die Idee geht in Richtung Bordeaux-Rot.
Generell:
(1) Sieht erstmal nach viel Beschreibung aus, bitte nicht entmutigen lassen, sind zu 90% nur austauschbare Inhalts-/Kontaktdaten.
(2) Für meine Zwecke reicht es vollkommen aus, wenn bei den Vorschlägen zur Arbeitsersparnis erstmal nur mit einer Adresse gearbeitet wird. Wenn ich dann den zutreffenden Designvorschlag gefunden habe, können wir die zweite Adresse in dem ersten Format umsetzen. Ich denke das spart Zeit und Nerven.
(3) Bitte Angaben wie "Tel.:" oder "USt.- ID:" nicht wörtlich nehmen, es soll dabei klar sein worum es geht; wenn "Telefon" ausgeschrieben besser aussieht, bitte in der optisch ansprechenderen Form verwenden.
(4) Bei Fragen, bitte fragen!
(5) Viel Spass bei dem Projekt - Ich freu' mich auf die Vorschläge!
Visitenkarten(1):
Juwelier Brandauer GmbH
www.juwelier-brandauer-example.de
Visitenkarten(2):
Visitenkarten(generell):
(1) Die einzelnen Daten können durch Hervorhebungen wie Adresse, Kontakt, Online/Internet unterteilt bzw. hervorgehoben werden.
(2) Die Visitenkarten sollen farbig gedruckt werden; geplant ist weiß als Hintergrund ist aber nicht zwingend bei einer guten anderen Idee
Briefpapier:
(1)Absender im Adressfeld für DIN-lang Briefumschläge mit Fenster:
(2)Informationen im Footer/Seitenbereich:
Juwelier Brandauer Gmb..

```html
<!DOCTYPE html>
<html lang="de">
<head>
<meta charset="utf-8">
<title>Juwelier Brandauer – Geschäftsausstattung</title>
<link href="https://fonts.googleapis.com/css2?family=Source+Sans+3:wght@300;400;600;700&display=swap" rel="stylesheet">
<style>
  :root {
    --plum: #4a1648;
    --grey: #8a8a8a;
    --rule: #c4c4c4;
    --ink: #2a2a2a;
  }
  * { margin: 0; padding: 0; box-sizing: border-box; }
  html, body { width: 872px; height: 1200px; overflow: hidden; }
  body {
    background: var(--plum);
    font-family: "Source Sans 3", sans-serif;
    position: relative;
    color: var(--ink);
  }
  .abs { position: absolute; }

  .brand { position: absolute; left: 0; right: 0; text-align: center; }
  .brand-square { display: block; margin: 0 auto; background: #fff; }
  .brand-name {
    display: block; font-weight: 600; color: var(--grey);
    letter-spacing: 0.02em; text-transform: uppercase; white-space: nowrap;
  }

  .hero-brand { top: 31px; }
  .hero-brand .brand-square { width: 49px; height: 88px; }
  .hero-brand .brand-name { font-size: 27px; margin-top: 18px; }

  .sheet { position: absolute; background: linear-gradient(180deg, #fafafa 0%, #d9d9d9 100%); }
  .sheet .brand-square { background: var(--plum); }
  .sheet.dark { background: var(--plum); border: 1px solid #d8c8d8; }
  .sheet.dark .brand-square { background: #fff; }
  .tab { position: absolute; bottom: -1px; left: 50%; transform: translateX(-50%); width: 14px; height: 8px; }
  .tab.plum { background: var(--plum); }
  .tab.grey { background: #777; }

  .small-brand .brand-square { width: 16px; height: 24px; }
  .small-brand .brand-name { font-size: 9px; margin-top: 9px; }

  .fine { font-size: 4.4px; line-height: 7.2px; text-align: center; color: var(--plum); white-space: nowrap; }
  .fine b { font-weight: 700; color: var(--grey); }
  .lbl { color: var(--grey); }

  /* A6 receipt */
  .receipt { left: 100px; top: 288px; width: 218px; height: 320px; }
  .receipt .rules { position: absolute; left: 27px; right: 27px; top: 94px; }
  .receipt .rules span { display: block; height: 12.6px; border-bottom: 1px solid var(--rule); }
  .receipt .policy { left: 0; right: 0; top: 243px; font-size: 4.6px; line-height: 6px; }
  .receipt .address { left: 0; right: 0; top: 275px; }

  .card-front { left: 336px; top: 288px; width: 178px; height: 118px; }
  .card-front-dark { left: 530px; top: 288px; width: 177px; height: 118px; }
  .card-back-a { left: 142px; top: 624px; width: 176px; height: 119px; }
  .card-back-b { left: 142px; top: 759px; width: 176px; height: 118px; }

  .card-brand .brand-square { width: 20px; height: 38px; }
  .card-brand .brand-name { font-size: 11px; margin-top: 10px; }
  .card-back .brand-square { width: 20px; height: 38px; }
  .card-back .fine { left: 0; right: 0; top: 48px; font-size: 4.3px; line-height: 6px; }

  /* A4 letterhead */
  .letter { left: 336px; top: 425px; width: 437px; height: 641px; font-size: 6.6px; line-height: 12.4px; font-weight: 300; }
  .letter .brand-square { width: 22px; height: 40px; }
  .letter .brand-name { font-size: 11.5px; margin-top: 10px; }
  .letter .sender { left: 50px; top: 108px; font-size: 4.2px; color: var(--plum); font-weight: 400; }
  .letter .contact { right: 49px; top: 108px; font-size: 4.2px; line-height: 6.5px; color: var(--plum); font-weight: 400; }
  .letter .recipient { left: 50px; top: 124px; line-height: 9px; font-size: 6.4px; font-style: normal; }
  .letter .recipient strong { font-weight: 600; }
  .letter .date { right: 49px; top: 215px; }
  .letter .subject { left: 0; right: 0; top: 227px; text-align: center; font-weight: 600; font-size: 6.6px; text-transform: uppercase; }
  .letter .body { left: 50px; right: 49px; top: 258px; }
  .letter .body p { margin-bottom: 12.4px; }
  .letter .footer { left: 0; right: 0; top: 601px; font-size: 4px; line-height: 6.5px; font-weight: 400; }
</style>
</head>
<body>

  <header class="brand hero-brand">
    <span class="brand-square"></span>
    <span class="brand-name">Juwelier Brandauer</span>
  </header>

  <section class="sheet receipt">
    <div class="brand small-brand" style="top:8px">
      <span class="brand-square"></span>
      <span class="brand-name">Juwelier Brandauer</span>
    </div>
    <div class="rules">
      <span></span><span></span><span></span><span></span><span></span><span></span><span></span><span></span><span></span><span></span>
    </div>
    <p class="fine abs policy">Bei Umtausch oder Reklamation bitte Beleg vorlegen.<br>Barauszahlung ganz oder teilweise ausgeschlossen.</p>
    <div class="fine abs address">
      <b>JUWELIER BRANDAUER GmbH</b><br>
      Goldschmiedgasse 12 in 45468 Mülheim a.d. Ruhr <span class="lbl">TEL</span> 0208-550123 <span class="lbl">FAX</span> 0208-550124<br>
      <span class="lbl">info@</span>juwelier-brandauer-example.de <span class="lbl">www.</span>juwelier-brandauer-example.de
    </div>
    <span class="tab plum"></span>
  </section>

  <section class="sheet card-front">
    <div class="brand card-brand" style="top:7px">
      <span class="brand-square" style="background:var(--grey)"></span>
      <span class="brand-name">Juwelier Brandauer</span>
    </div>
    <span class="tab plum"></span>
  </section>

  <section class="sheet dark card-front-dark">
    <div class="brand card-brand" style="top:7px">
      <span class="brand-square"></span>
      <span class="brand-name">Juwelier Brandauer</span>
    </div>
    <span class="tab grey"></span>
  </section>

  <section class="sheet card-back card-back-a">
    <div class="brand" style="top:7px"><span class="brand-square"></span></div>
    <div class="fine abs">
      <b>JUWELIER BRANDAUER GmbH</b><br>
      Goldschmiedgasse 12 in 45468 Mülheim a.d. Ruhr<br>
      <span class="lbl">TEL</span> 0208-550123 <span class="lbl">FAX</span> 0208-550124 <span class="lbl">info@</span>juwelier-brandauer-example.de<br>
      www.juwelier-brandauer-example.de
    </div>
    <span class="tab grey"></span>
  </section>

  <section class="sheet card-back card-back-b">
    <div class="brand" style="top:7px"><span class="brand-square" style="background:var(--grey)"></span></div>
    <div class="fine abs">
      <b>JUWELIER BRANDAUER GmbH</b><br>
      Goldschmiedgasse 12 in 45468 Mülheim a.d. Ruhr<br>
      <span class="lbl">TEL</span> 0208-550123 <span class="lbl">FAX</span> 0208-550124 <span class="lbl">info@</span>juwelier-brandauer-example.de<br>
      www.juwelier-brandauer-example.de
    </div>
    <span class="tab plum"></span>
  </section>

  <section class="sheet letter">
    <div class="brand" style="top:14px">
      <span class="brand-square"></span>
      <span class="brand-name">Juwelier Brandauer</span>
    </div>
    <p class="abs sender"><span class="lbl">JUWELIER BRANDAUER GmbH</span>&nbsp; Goldschmiedgasse 12 in 45468 Mülheim a.d. Ruhr</p>
    <p class="abs contact"><span class="lbl">TEL</span> 0208-550123 <span class="lbl">FAX</span> 0208-550124 <span class="lbl">info@</span>juwelier-brandauer-example.de<br><span class="lbl">www.</span>juwelier-brandauer-example.de</p>
    <address class="abs recipient">
      Frau<br><strong>Marlene Topasius</strong><br>Saphirweg 14<br><br>45468 Mülheim an der Ruhr
    </address>
    <p class="abs date">Mülheim, den 03. 05. 2014</p>
    <h1 class="abs subject">Diamantstaub am Horizont</h1>
    <div class="abs body">
      <p>Sehr geehrte Frau Topasius,</p>
      <p>hier schreibe ich einen Blindtext dahin: Diamanten, die groß genug für die Schmuckproduktion sind, bilden sich nur im Erdmantel unter hohen Drücken und Temperaturen, typischerweise in Tiefen zwischen 150 bis 660 Kilometern und bei Temperaturen von 1200 bis 1400 °C. Diamant-Muttergesteine im Erdmantel sind Peridotit und Eklogit. Letzterer kann versenkte ozeanische Kruste repräsentieren.</p>
      <p>Die jeweilige Transportdauer aus der Tiefe wird auf wenige Stunden geschätzt, sodass aufgrund der Schnelligkeit keine Phasenumwandlung zu Graphit stattfindet. Die letzte Phase der Eruption erfolgt mit Überschallgeschwindigkeit. Diamanten sind Fremd- oder Xenokristalle in Kimberlit und Lamproit und in diesen Magmen chemisch nicht stabil (metastabil).</p>
      <p>So kann man an natürlichen Diamanten immer Auflösungserscheinungen beobachten. Von ihren Vorkommen in Pipes können die Diamantkristalle durch natürliche Verwitterungsprozesse, bei denen sie aufgrund ihrer Härte intakt bleiben, abtransportiert und in Sedimentgesteinen angereichert werden, die heute eine der Hauptquellen dieses Minerals darstellen.</p>
      <p>Mit den allerbesten Grüßen</p>
      <p>Clara Opalski</p>
    </div>
    <div class="abs fine footer">
      <span class="lbl">Juwelier Brandauer GmbH</span>&nbsp; Goldschmiedgasse 12 in 45468 Mülheim a.d. Ruhr<br>
      <span class="lbl">Geschäftsführer</span> Henrike Brandauer&nbsp; <span class="lbl">Amtsgericht Musterstadt</span> HRB 00000&nbsp; <span class="lbl">Steuernummer</span> 000/0000/0000&nbsp; <span class="lbl">USt.-ID</span> DE 000000000<br>
      <span class="lbl">Bank</span> Beispielbank AG&nbsp; <span class="lbl">IBAN</span> DE00 0000 0000 0000 0000 00&nbsp; <span class="lbl">BIC</span> BSPL DE 00
    </div>
    <span class="tab grey"></span>
  </section>

</body>
</html>
```